Eye catching Stationary Design

Healthcare consultant firm looking for stationary design ( letterhead, envelope and business cards) That’s professional, classy and eye catching . The design should incorporate the logo and the colors of the logo in its design. You can see the logo on our website at www crestmore advisory. net.

```html
<!DOCTYPE html>
<html lang="en">
<head>
<meta charset="utf-8">
<title>Crestmore Advisory – Business Card</title>
<link rel="stylesheet" href="https://fonts.googleapis.com/css2?family=Lato:wght@400;700&display=swap">
<style>
  :root {
    --page-bg: #e9e6e1;
    --card-bg: #f4f5f6;
    --panel-deep: #0c3b73;
    --panel-mid: #1b5a9a;
    --panel-light: #2c6fb0;
    --accent-teal: #17899a;
    --name-teal: #3aa6b4;
    --panel-text: #cfdbe9;
    --brand-navy: #12355f;
  }
  * { margin: 0; padding: 0; box-sizing: border-box; }
  html, body {
    width: 1200px; height: 1047px; overflow: hidden;
    background: var(--page-bg);
    font-family: "Lato", Arial, sans-serif;
  }
  .business-card {
    position: absolute; left: 110px; top: 243px;
    width: 980px; height: 560px;
    border-radius: 26px; overflow: hidden;
    background: var(--card-bg);
    box-shadow: 0 10px 30px rgba(0,0,0,0.12);
  }
  .card-shapes { position: absolute; inset: 0; }
  .contact-side {
    position: absolute; left: 39px; top: 0;
    color: var(--panel-text);
  }
  .holder-name {
    position: absolute; top: 76px; left: 0; white-space: nowrap;
    font-size: 40px; font-weight: 700; letter-spacing: 0.5px;
    color: var(--name-teal);
  }
  .holder-role {
    position: absolute; top: 136px; left: 0; white-space: nowrap;
    font-size: 22px;
  }
  .postal-address {
    position: absolute; top: 250px; left: 0; white-space: nowrap;
    font-size: 22px; font-style: normal; line-height: 32px;
  }
  .contact-list { position: absolute; top: 338px; left: 0; list-style: none; }
  .contact-item {
    display: flex; align-items: center; gap: 18px;
    height: 36.5px; font-size: 22px; white-space: nowrap;
  }
  .contact-icon { width: 26px; height: 26px; flex: none; }
  .brand-lockup {
    position: absolute; left: 560px; width: 420px; top: 250px;
    display: flex; align-items: center; justify-content: center; gap: 14px;
  }
  .brand-dot {
    width: 22px; height: 22px; border-radius: 50%;
    background: var(--brand-navy);
  }
  .brand-name {
    font-size: 30px; font-weight: 700; color: var(--brand-navy);
    letter-spacing: 0.4px; white-space: nowrap;
  }
</style>
</head>
<body>
  <div class="business-card">
    <svg class="card-shapes" width="980" height="560" viewBox="0 0 980 560" aria-hidden="true">
      <defs>
        <linearGradient id="panelFill" x1="0" y1="0" x2="1" y2="1">
          <stop offset="0" stop-color="var(--panel-light)"/>
          <stop offset="0.55" stop-color="var(--panel-mid)"/>
          <stop offset="1" stop-color="var(--panel-deep)"/>
        </linearGradient>
      </defs>
      <path d="M0 0 H560 Q440 280 560 560 H0 Z" fill="var(--accent-teal)"/>
      <path d="M0 0 H540 Q425 280 540 560 H0 Z" fill="url(#panelFill)"/>
    </svg>

    <div class="contact-side">
      <h1 class="holder-name">DANIEL REYES</h1>
      <p class="holder-role">Founder &amp; CEO</p>
      <address class="postal-address">1234 First Line Address<br>5678 Second Line Address</address>
      <ul class="contact-list">
        <li class="contact-item">
          <svg class="contact-icon" viewBox="0 0 24 24" fill="none" stroke="var(--name-teal)" stroke-width="1.8" stroke-linecap="round" stroke-linejoin="round"><path d="M5 3h4l2 5-2.5 1.5a11 11 0 0 0 6 6L16 13l5 2v4a2 2 0 0 1-2 2A17 17 0 0 1 3 5a2 2 0 0 1 2-2z"/></svg>
          <span>(555) 214-0387</span>
        </li>
        <li class="contact-item">
          <svg class="contact-icon" viewBox="0 0 24 24" fill="none" stroke="var(--name-teal)" stroke-width="1.8" stroke-linejoin="round"><rect x="2.5" y="5" width="19" height="14"/><path d="M2.5 5l9.5 8 9.5-8"/></svg>
          <span>info@crestmoreadvisory.net</span>
        </li>
        <li class="contact-item">
          <svg class="contact-icon" viewBox="0 0 24 24" fill="none" stroke="var(--name-teal)" stroke-width="1.6"><circle cx="12" cy="12" r="9.5"/><ellipse cx="12" cy="12" rx="4" ry="9.5"/><path d="M2.5 12h19M4 7h16M4 17h16"/></svg>
          <span>www.crestmoreadvisory.net</span>
        </li>
      </ul>
    </div>

    <div class="brand-lockup">
      <span class="brand-dot"></span>
      <span class="brand-name">Crestmore Advisory LLC</span>
    </div>
  </div>
</body>
</html>
```